Need Letterhead and Business Card

I have a logo but i need new letterhead and biz cards. We are a real estate investment firm so we need very professional but also do not want to be old fashioned. We have 3 locations; Singapore, New York and Ponte Vedra Florida. I can provide full addresses if needed. If you have adjustments to our logo you would recommend we are open to them.
I will be putting in a separate project but we also need a template for our own powerpoint slide presentations and website.

Real Estate

```html
<!DOCTYPE html>
<html lang="en">
<head>
<meta charset="utf-8">
<title>Halvern Letterhead</title>
<link rel="stylesheet" href="https://fonts.googleapis.com/css2?family=Arimo:wght@400;700&display=swap">
<style>
  :root {
    --navy: #2f3f6b;
    --gold: #c49a3c;
    --ink: #1f1f24;
    --paper: #ffffff;
    --band-top: #ffffff;
    --band-bottom: #8c8aa9;
  }
  * { margin: 0; padding: 0; box-sizing: border-box; }
  html, body {
    width: 876px;
    height: 1200px;
    overflow: hidden;
    background: var(--paper);
  }
  .letterhead {
    position: relative;
    width: 876px;
    height: 1200px;
    background: var(--paper);
    font-family: "Arimo", Arial, sans-serif;
  }
  .brand {
    position: absolute;
    top: 40px;
    right: 31px;
    width: 252px;
    text-align: right;
  }
  .brand-name {
    display: block;
    color: var(--navy);
    font-weight: 700;
    font-size: 46px;
    line-height: 56px;
    letter-spacing: 1px;
  }
  .brand-rule {
    display: block;
    height: 2px;
    margin-top: 6px;
    background: var(--navy);
  }
  .brand-tagline {
    display: block;
    margin-top: 7px;
    color: var(--gold);
    font-size: 11.5px;
    line-height: 14px;
    letter-spacing: 0;
    white-space: nowrap;
  }
  .contact-band {
    position: absolute;
    left: 0;
    bottom: 0;
    width: 876px;
    height: 92px;
    background: linear-gradient(to bottom, var(--band-top) 0%, var(--band-bottom) 100%);
  }
  .contact-details {
    position: absolute;
    left: 0;
    right: 35px;
    bottom: 11px;
    text-align: center;
    color: var(--ink);
    font-size: 13.5px;
    line-height: 16.5px;
    font-style: normal;
  }
</style>
</head>
<body>
  <main class="letterhead">
    <header class="brand">
      <span class="brand-name">HALVERN</span>
      <span class="brand-rule"></span>
      <span class="brand-tagline">REAL ESTATE INVESTMENT &amp; MANAGEMENT</span>
    </header>

    <footer class="contact-band">
      <address class="contact-details">
        Address<br>
        Telephone numbers<br>
        Web site
      </address>
    </footer>
  </main>
</body>
</html>
```